This book will apply the 12 Steps to gaming addiction, also known as video game addiction. The primary purpose of the book is to provide an effective solution for this new type of addiction. The solution is based on the rich and successful concepts of traditional twelve-step programs like RL.

The title on the cover will be "Nine Doors Past the Glowing Screen" and "by Martin Quorby". A subtitle can be used if it works in your design of "A Practical Path Beyond Compulsive Console Play". Cover will be for a 6" x 9" book approximately 110 pages in length.

Some back cover text including some review quotes and an author bio are in the attached Word doc. There is also an author photo attached for for the back cover.

Requirements
Must have
• For the cover design it could be stylized, or an image, a partial image, or whatever. I am open to suggestions. Think about what would be noticed by a person searching for help with moderating their video game use, or by the parents or loved ones of problem gamers. Something contemporary and eye catching.

```html
<!DOCTYPE html>
<html lang="en">
<head>
<meta charset="utf-8">
<title>Nine Doors Past the Glowing Screen — Cover</title>
<link rel="stylesheet" href="https://fonts.googleapis.com/css2?family=Montserrat:wght@300;400;500;600&display=swap">
<style>
  :root {
    --slate: #4e6264;
    --frame-blue: #a9d1e3;
    --ink-light: #f2f4f4;
    --spine-ink: #d9dfe0;
    --gold-line: #f3d36b;
    --white: #ffffff;
  }
  * { margin: 0; padding: 0; box-sizing: border-box; }
  html, body { width: 1200px; height: 893px; overflow: hidden; background: var(--slate); }
  .cover {
    position: relative; width: 1200px; height: 893px;
    font-family: "Montserrat", sans-serif; color: var(--ink-light);
    background: var(--slate);
  }

  /* Back cover */
  .back-frame {
    position: absolute; left: 36px; top: 36px; width: 488px; height: 822px;
    border: 3px solid var(--frame-blue);
  }
  .back-block { position: absolute; left: 57px; width: 448px; font-weight: 300;
    font-size: 12.4px; line-height: 13.2px; letter-spacing: -0.35px; }
  .praise-heading { position: absolute; left: 57px; top: 57px; font-size: 13.6px;
    font-weight: 500; letter-spacing: -0.3px; color: var(--white); }
  .quote-source { display: block; font-style: italic; }
  .quote-source.plain { font-style: normal; }
  .divider { position: absolute; left: 97px; top: 311px; width: 352px; height: 1.5px;
    background: var(--ink-light); }
  .author-photo { position: absolute; left: 57px; top: 584px; width: 104px; height: 96px;
    border-radius: 50%;
    background: radial-gradient(circle at 50% 45%, #8a6f5c 0%, #5b6a4e 55%, #2c3a2c 100%); }
  .author-bio { position: absolute; left: 184px; top: 581px; width: 320px; font-weight: 500;
    font-size: 12.2px; line-height: 13.2px; letter-spacing: -0.3px; color: var(--white); }
  .isbn-box { position: absolute; left: 65px; top: 706px; width: 183px; height: 121px;
    background: var(--white); }

  /* Spine */
  .spine-title, .spine-author {
    position: absolute; left: 586px; writing-mode: vertical-rl;
    font-weight: 300; font-size: 18px; letter-spacing: 1.2px; color: var(--spine-ink);
    white-space: nowrap;
  }
  .spine-title { top: 108px; }
  .spine-author { top: 651px; }

  /* Front cover */
  .front-art { position: absolute; left: 642px; top: 0; width: 558px; height: 893px;
    background:
      radial-gradient(ellipse at 52% 30%, #fff2b0 0%, #f7a635 18%, #d9611d 40%, rgba(140,80,40,0) 62%),
      linear-gradient(180deg, #7c8a32 0%, #c66b22 25%, #a7572f 45%, #8a6f5e 62%, #7d7870 80%, #8c8680 100%); }
  .front-frame { position: absolute; left: 677px; top: 36px; width: 487px; height: 821px;
    border: 2px solid var(--gold-line); }
  .front-title { position: absolute; left: 642px; top: 104px; width: 558px; text-align: center;
    font-weight: 400; font-size: 54px; line-height: 74px; letter-spacing: 5px;
    color: var(--white); text-transform: uppercase; }
  .front-author { position: absolute; left: 878px; top: 540px; font-weight: 400;
    font-size: 26px; line-height: 34px; letter-spacing: 3px; color: var(--white);
    text-transform: uppercase; }
</style>
</head>
<body>
<div class="cover">
  <!-- Back cover -->
  <div class="back-frame"></div>
  <h2 class="praise-heading">Praise for Nine Doors Past the Glowing Screen</h2>

  <p class="back-block" style="top:86px">“A must-read for anyone who is addicted to or thinks they may have a problem with digital gaming. This eloquent work will also be useful to academics and clinicians exploring potential solutions. The author recognizes the similarities between gaming addiction and other addictions, and logically applies one of the most effective known solutions for addiction - The Twelve Steps.”
    <span class="quote-source">-- Dale Penwright, Noted Interventionist and Keynote Speaker</span></p>

  <p class="back-block" style="top:178px">“If you suffer from digital gaming addiction, I strongly encourage you to use this book as your road map to get you back to the real world.”
    <span class="quote-source plain">-- Owen Tarrabee, Founder of Feedline Review.</span>
    “As a high school teacher for 24 years, husband, father, coach, and 12-Step member, I can assure you that this book will transform the life of anyone who is addicted to video games. Well written, easy to understand, and a wonderful book that will provide you with a clear road map to recovery, and this includes teenagers, a group I have been working with in the classroom for decades.”
    <span class="quote-source">-- Elias Morrow, Harbor Vale, OR High School Teacher.</span></p>

  <div class="divider"></div>

  <p class="back-block" style="top:323px">A practical path beyond compulsive console play (aka Video Game Addiction) based on the rich and successful tradition of the Twelve Steps.</p>

  <p class="back-block" style="top:362px">Addiction to Digital Gaming is a new and troubling phenomenon that has burst upon an unprepared society with alarming speed. Many people crave the use of Digital Games in a strikingly similar way to any other addict. Digital Games are a complex software and hardware system that have been designed to promote continued and progressive usage. This sophisticated technology clearly feeds on natural addictive tendencies.</p>

  <p class="back-block" style="top:455px">The 12 Steps are one of the most effective methods for treating addiction in human history. Originating with Recovery League in 1939, the 12 Steps have since been used to treat a variety of other addictions, including drugs, sex, gambling, eating disorders, and many others. Now in this groundbreaking work the 12 Steps are applied to the complex and evolving contemporary phenomenon of Digital Gaming Addiction.</p>

  <div class="author-photo" role="img" aria-label="Author portrait photo"></div>
  <p class="author-bio">Marty Quorby is a Technology Consultant and Writer with many years of professional coding and consulting experience. He also struggled with addiction to drugs and alcohol and is now clean and sober in a Twelve-Step program for over 17 years. This unique combination of 12-Step experience and technology expertise led him to create Nine Doors Past the Glowing Screen.</p>
  <div class="isbn-box"></div>

  <!-- Spine -->
  <div class="spine-title">NINE DOORS PAST THE GLOWING SCREEN</div>
  <div class="spine-author">MARTIN QUORBY</div>

  <!-- Front cover -->
  <div class="front-art" role="img" aria-label="Sunlit autumn trees above a stone staircase, with hands holding a game controller, wrists bound by its cable"></div>
  <div class="front-frame"></div>
  <h1 class="front-title">Nine Doors<br>Past the<br>Glowing<br>Screen</h1>
  <p class="front-author">Martin<br>Quorby</p>
</div>
</body>
</html>
```